Product Setup Instructional Infographic/flyer

Converting product instructions into an infographic. Would prefer that the instructions fit on a 4x6 card, front and back, but a slightly larger size is acceptable as well.

Logo Text

Ridgeline Cask (Rebranding just as Ridgeline Cask, instead of Ridgeline Cask Barrels)

Font styles to use
Decorative

Colors

Designer to choose colors to be used in the design.

Requirements
Must have
• NA
Nice to have
• NA
Should not have
• NA

```html
<!DOCTYPE html>
<html lang="en">
<head>
<meta charset="utf-8">
<title>Oak Barrel Curing Guide</title>
<link href="https://fonts.googleapis.com/css2?family=Montserrat:wght@400;500;800;900&family=Roboto+Condensed:wght@400;700&display=swap" rel="stylesheet">
<style>
:root{
  --red:#d0121b;
  --red-dark:#a50d14;
  --blue:#0b62b0;
  --blue-dark:#074a88;
  --ink:#2b2b2b;
  --panel:#f0f0f0;
  --rail:#e2e2e2;
  --stage:#c8c8c8;
  --paper:#ffffff;
}
*{margin:0;padding:0;box-sizing:border-box}
html,body{width:1200px;height:888px;overflow:hidden}
body{background:var(--stage);position:relative;font-family:"Roboto Condensed",Arial,sans-serif;color:var(--ink)}
.page{position:absolute;top:32px;width:532px;height:794px;background:var(--paper);box-shadow:0 18px 22px -10px rgba(0,0,0,.45);overflow:hidden}
.page--front{left:42px}
.page--back{left:626px}
.page__band{position:absolute;left:0;top:0;width:100%;height:16px;background:var(--blue)}
.page__arc{position:absolute;left:0;bottom:0;width:100%;height:22px}
.page-label{position:absolute;top:846px;width:532px;text-align:center;font-family:"Montserrat",Arial,sans-serif;font-weight:500;font-size:16px;letter-spacing:.5px;color:#222}
.page-label--front{left:42px}
.page-label--back{left:626px}

.title{position:absolute;left:0;top:34px;width:100%;text-align:center;font-family:"Montserrat",Arial,sans-serif;font-weight:900;font-size:37px;line-height:40px;color:var(--red);letter-spacing:-.3px;white-space:nowrap}
.title-rule{position:absolute;left:40px;top:78px;width:454px;border-top:2px dashed var(--red)}
.subtitle{position:absolute;left:0;top:89px;width:100%;text-align:center;font-family:"Montserrat",Arial,sans-serif;font-weight:400;font-size:25px;line-height:30px;color:#1b1b1b;white-space:nowrap}
.subtitle-strong{position:absolute;left:0;top:121px;width:100%;display:flex;align-items:center;justify-content:center;gap:10px;font-family:"Montserrat",Arial,sans-serif;font-weight:800;font-size:25px;line-height:30px;color:#1b1b1b;white-space:nowrap}
.subtitle-line{display:block;width:72px;height:2px;background:var(--red)}

.thanks-rail{position:absolute;left:0;top:206px;width:100%;height:5px;background:var(--blue)}
.thanks{position:absolute;left:50px;top:170px;width:432px;height:76px;background:var(--blue);clip-path:polygon(9% 0,91% 0,100% 50%,91% 100%,9% 100%,0 50%);color:#fff;text-align:center;font-size:13px;line-height:18px;padding:11px 56px 0}
.intro{position:absolute;left:27px;top:264px;width:482px;font-size:13px;line-height:20px}

.timeline{position:absolute;left:428px;width:7px;background:var(--rail);border-radius:4px}
.step{position:absolute;left:26px;width:340px}
.step__panel{position:absolute;left:12px;top:8px;right:0;bottom:0;background:var(--panel);border-radius:18px 0 0 18px}
.step__fold{position:absolute;right:-36px;width:36px;height:38px;background:linear-gradient(135deg,#9a9a9a,#c9c9c9);clip-path:polygon(0 0,100% 0,0 100%)}
.step__tab{position:absolute;left:0;top:0;width:124px;height:74px}
.step__icon{position:absolute;left:16px;top:18px;width:40px;height:38px;border-radius:6px;background:rgba(255,255,255,.85)}
.step__text{position:absolute;left:110px;top:18px;width:218px;font-size:12.4px;line-height:18.4px;color:#333}
.marker{position:absolute;left:420px;width:23px;height:23px;border-radius:50%}
.marker--red{background:radial-gradient(circle,var(--red-dark) 45%,var(--red) 50%)}
.marker--blue{background:radial-gradient(circle,var(--blue-dark) 45%,var(--blue) 50%)}
.step-label{position:absolute;left:455px;font-weight:700;font-size:16px;line-height:1}
.step-label--red{color:var(--red)}
.step-label--blue{color:var(--blue)}

.tip-head{position:absolute;left:26px;top:607px;width:479px;height:39px;background:var(--blue);color:#fff;text-align:center;font-family:"Montserrat",Arial,sans-serif;font-weight:900;font-size:28px;line-height:39px;letter-spacing:.3px}
.tip-body{position:absolute;left:28px;top:654px;width:474px;height:90px;background:var(--panel);box-shadow:0 10px 10px -6px rgba(0,0,0,.25);font-size:13px;line-height:20px;padding:11px 16px 0 20px;color:#222}
.tip-corner{position:absolute;height:28px;border-color:var(--blue);border-style:solid}
.tip-corner--tr{left:486px;top:650px;border-width:3px 3px 0 0;width:24px}
.tip-corner--bl{left:26px;top:716px;border-width:0 0 3px 3px;width:24px}
</style>
</head>
<body>

<section class="page page--front">
  <div class="page__band"></div>
  <h1 class="title">A STEP BY STEP GUIDE</h1>
  <div class="title-rule"></div>
  <p class="subtitle">ON HOW TO CURE YOUR</p>
  <p class="subtitle-strong"><span class="subtitle-line"></span>OAK BARREL<span class="subtitle-line"></span></p>

  <div class="thanks-rail"></div>
  <p class="thanks">First, we would like to thank you for choosing Ridgeline Cask Barrels for your home spirit and wine - aging needs. We know you are very excited to use it and so are we.</p>

  <p class="intro">However, your barrel is NOT ready yet for use. You need to cure it first to get rid of the wood debris and make it watertight. Do not fret, we laid out an easy to follow step by step guide on how to ready your barrel for spirit and wine-aging.</p>

  <div class="timeline" style="top:358px;height:388px"></div>

  <div class="step" style="top:350px;height:82px">
    <div class="step__panel"></div>
    <div class="step__fold" style="top:44px"></div>
    <svg class="step__tab" viewBox="0 0 124 74"><path d="M18 0H112L124 6C98 8 92 74 58 74H18Q0 74 0 56V18Q0 0 18 0Z" fill="var(--red)"/></svg>
    <div class="step__icon" role="img" aria-label="Wooden log icon"></div>
    <p class="step__text">Rinse and soak the spigot (wooden faucet) and the plug (or bung) in water for about half an hour.</p>
  </div>
  <span class="marker marker--red" style="top:383px"></span>
  <span class="step-label step-label--red" style="top:387px">STEP 01</span>

  <div class="step" style="top:456px;height:162px">
    <div class="step__panel"></div>
    <div class="step__fold" style="top:124px"></div>
    <svg class="step__tab" viewBox="0 0 124 74"><path d="M18 0H112L124 6C98 8 92 74 58 74H18Q0 74 0 56V18Q0 0 18 0Z" fill="var(--blue)"/></svg>
    <div class="step__icon" role="img" aria-label="Saw cutting wood icon"></div>
    <p class="step__text">While waiting, fill the barrel with water until it is half-full. Use your thumb to plug the holes, give it a good shake to get rid of wood chips and debris that might be trapped inside. Let the water out. You may repeat this process three to five times until you satisfied the barrel is thoroughly clean.</p>
  </div>
  <span class="marker marker--blue" style="top:571px"></span>
  <span class="step-label step-label--blue" style="top:575px">STEP 02</span>

  <div class="step" style="top:644px;height:102px">
    <div class="step__panel"></div>
    <div class="step__fold" style="top:64px"></div>
    <svg class="step__tab" viewBox="0 0 124 74"><path d="M18 0H112L124 6C98 8 92 74 58 74H18Q0 74 0 56V18Q0 0 18 0Z" fill="var(--red)"/></svg>
    <div class="step__icon" role="img" aria-label="Axe in tree stump icon"></div>
    <p class="step__text">Plug the barrel with the spigot. You may tighten it securely with your hand. We advise not to use a hammer as it may crack the wood.</p>
  </div>
  <span class="marker marker--red" style="top:699px"></span>
  <span class="step-label step-label--red" style="top:703px">STEP 03</span>

  <svg class="page__arc" viewBox="0 0 532 22" preserveAspectRatio="none"><path d="M30 22Q266 -8 502 22Z" fill="var(--blue)"/></svg>
</section>

<section class="page page--back">
  <div class="page__band"></div>
  <div class="timeline" style="top:50px;height:511px"></div>

  <div class="step" style="top:42px;height:81px">
    <div class="step__panel"></div>
    <div class="step__fold" style="top:43px"></div>
    <svg class="step__tab" viewBox="0 0 124 74"><path d="M18 0H112L124 6C98 8 92 74 58 74H18Q0 74 0 56V18Q0 0 18 0Z" fill="var(--blue)"/></svg>
    <div class="step__icon" role="img" aria-label="Barrel icon"></div>
    <p class="step__text" style="top:24px">Place the barrel in a sink, tub, or any place that is OK to get wet.</p>
  </div>
  <span class="marker marker--blue" style="top:75px"></span>
  <span class="step-label step-label--blue" style="top:79px">STEP 04</span>

  <div class="step" style="top:150px;height:120px">
    <div class="step__panel"></div>
    <div class="step__fold" style="top:82px"></div>
    <svg class="step__tab" viewBox="0 0 124 74"><path d="M18 0H112L124 6C98 8 92 74 58 74H18Q0 74 0 56V18Q0 0 18 0Z" fill="var(--red)"/></svg>
    <div class="step__icon" role="img" aria-label="Funnel icon"></div>
    <p class="step__text">Using a funnel, fill the barrel with hot water until it is full. Leave the top hole open. Your barrel might leak, and that's OK. It is not watertight yet and this process will make the wood expand to seal the gaps.</p>
  </div>
  <span class="marker marker--red" style="top:222px"></span>
  <span class="step-label step-label--red" style="top:226px">STEP 05</span>

  <div class="step" style="top:294px;height:137px">
    <div class="step__panel"></div>
    <div class="step__fold" style="top:99px"></div>
    <svg class="step__tab" viewBox="0 0 124 74"><path d="M18 0H112L124 6C98 8 92 74 58 74H18Q0 74 0 56V18Q0 0 18 0Z" fill="var(--blue)"/></svg>
    <div class="step__icon" role="img" aria-label="Drum icon"></div>
    <p class="step__text">Leave the barrel this way until no more leakages can be seen. This means the wood has expanded and the gaps are sealed. This can take from 30 minutes to an entire week, depending on the size of the barrel.</p>
  </div>
  <span class="marker marker--blue" style="top:387px"></span>
  <span class="step-label step-label--blue" style="top:391px">STEP 06</span>

  <div class="step" style="top:458px;height:103px">
    <div class="step__panel"></div>
    <div class="step__fold" style="top:65px"></div>
    <svg class="step__tab" viewBox="0 0 124 74"><path d="M18 0H112L124 6C98 8 92 74 58 74H18Q0 74 0 56V18Q0 0 18 0Z" fill="var(--red)"/></svg>
    <div class="step__icon" role="img" aria-label="Draining barrel icon"></div>
    <p class="step__text">Drain the barrel and let it air dry for no more than four hours. After 4 hours, it is ready to be filled with any spirits or wine of your choice.</p>
  </div>
  <span class="marker marker--red" style="top:513px"></span>
  <span class="step-label step-label--red" style="top:517px">STEP 07</span>

  <h2 class="tip-head">ADDITIONAL TIP</h2>
  <span class="tip-corner tip-corner--tr"></span>
  <span class="tip-corner tip-corner--bl"></span>
  <p class="tip-body">If you plan on aging different kinds of alcohol using the same barrel, you must cure the barrel again (Step 6) for three to five days. This will allow the barrel to absorb enough water and prevent the next batch of alcohol from being contaminated.</p>

  <svg class="page__arc" viewBox="0 0 532 22" preserveAspectRatio="none"><path d="M30 22Q266 -8 502 22Z" fill="var(--blue)"/></svg>
</section>

<p class="page-label page-label--front">FRONT</p>
<p class="page-label page-label--back">BACK</p>

</body>
</html>
```